Flyer Design for a Boston Therapeutic Clinic

I am a body therapist who needs a couple of flyers designed:
1. To fit half a page.
2. To fit a 5 inch by 3.5 inch flyer.
My practice is based in Boston, MA and my web site is:
www.LarkfieldTane.Com
For the First half page:
A. Have my company's name and color shown as it appears on my web site (Larkfield Tane)
B. Have the following text: "Control your weight (This part should be emphasized) by balancing your nervous and digestive system through the Tane Method. The Tane Method, a technique developed by Dr. Wenna. Tane, uses physical pressure to manipulate visceral tissue to bring back resiliency and proper functioning of the whole body."
Also helps with
-Constipation
-Bloating
-IBS
-eating disorders and overeating
Our practitioner is highly experienced. Please visit our web sites for reviews.
C. I would like to have a nice earthy feeling, something that feels "freeing" like open flowers, or an open land scape such as mountains or fields.
D. I also like the color blue, white, orange; perhaps if these colors can be integrated into the flyer, that would be great.
E. "Visit our web site LarkfieldTane.com or call 413-908-2617"
The Smaller Flyer :
A.The smaller Flyer should also have my Company's name as shown on my web site (Larkfield Tane)
B.The following text: " Restore your body's natural resiliency and greatly reduce your physical pain through the Dr. Wenna Tane Method of Structural Integration."
C. "Our practitioner is highly experienced and has a great reputation; visit our web site for reviews."
"Benefits:
"reduce aches and pains
reduce joint pain
reduce chronic muscular tension"
D, "feel better after the first session!"
E. if you could use a picture of me working on someone from my web site, that would be great.
F. I also like the colors white, orange and silver, for this one.
G. "Visit our web site LarkfieldTane.com or call 413-908 2617"
I am very open minded,
I would like the flyer to evoke a sense of tranquility, professionalism, and simplicity. So if you have another angle you think would look good, then go for it! As long as it looks clean, professional and helpful.
Thanks a lot!
If you need any pictures from my web site, I have the original high resolution files that i can send.
Professionals and working men and women from ages 20-70
Clinic

```html
<!DOCTYPE html>
<html lang="en">
<head>
<meta charset="utf-8">
<title>Larkfield Tane Therapy – Flyers</title>
<link rel="stylesheet" href="https://fonts.googleapis.com/css2?family=Bebas+Neue&family=Roboto+Slab:wght@300;400;700&family=Arimo:wght@400;700&display=swap">
<style>
  :root {
    --blue-deep: #0a4a9e;
    --blue-mid: #1670cf;
    --blue-glow: #c9efff;
    --navy: #062a5c;
    --orange: #f26235;
    --grey-shadow: #c9c9c9;
    --ink: #111111;
    --white: #ffffff;
    --skin: #d9a58c;
    --skin-dark: #7a4a35;
  }
  * { margin: 0; padding: 0; box-sizing: border-box; }
  html, body { width: 1200px; height: 943px; overflow: hidden; background: var(--white); }
  body { position: relative; font-family: "Roboto Slab", Georgia, serif; }

  .format-label {
    position: absolute;
    font-family: "Bebas Neue", "Arial Narrow", sans-serif;
    color: var(--ink);
    transform: translateX(-50%);
    white-space: nowrap;
  }
  .format-label--large { left: 331px; top: 28px; font-size: 23px; }
  .format-label--small { left: 848px; top: 176px; font-size: 17px; }

  .flyer {
    position: absolute;
    overflow: hidden;
    background: var(--white);
    border: 1px solid #8a8a8a;
    box-shadow: 14px 16px 26px rgba(0,0,0,0.35);
  }
  .flyer--half { left: 83px; top: 66px; width: 513px; height: 767px; }
  .flyer--small { left: 674px; top: 203px; width: 358px; height: 537px; box-shadow: 10px 12px 20px rgba(0,0,0,0.35); }

  .sky {
    position: absolute; left: 0; top: 0; width: 100%;
    background:
      radial-gradient(ellipse 45% 40% at 90% 85%, var(--blue-glow) 0%, rgba(120,200,255,0.55) 35%, rgba(22,112,207,0) 75%),
      linear-gradient(180deg, var(--blue-deep) 0%, var(--blue-mid) 70%, #2a8ee6 100%);
  }
  .flyer--half .sky { height: 560px; }
  .flyer--small .sky { height: 400px; }

  .photo { position: absolute; }
  .flyer--half .photo {
    left: 262px; top: 0; width: 251px; height: 219px;
    background: radial-gradient(ellipse 70% 75% at 60% 45%, var(--skin) 0%, #c99580 45%, rgba(201,149,128,0) 85%);
  }
  .flyer--small .photo {
    left: 36px; top: 2px; width: 322px; height: 212px;
    background: radial-gradient(ellipse 70% 70% at 65% 45%, #c48668 0%, var(--skin-dark) 45%, rgba(40,30,40,0.2) 80%, rgba(22,112,207,0) 100%);
  }

  .headline {
    position: absolute;
    font-family: "Bebas Neue", "Arial Narrow", sans-serif;
    font-weight: 400;
    color: var(--white);
    text-shadow: 2px 3px 5px rgba(0,0,0,0.45);
    text-transform: uppercase;
    white-space: nowrap;
  }
  .flyer--half .headline { left: 45px; top: 34px; font-size: 80px; line-height: 75px; }
  .flyer--small .headline { left: 29px; top: 48px; font-size: 31px; line-height: 33px; }

  .rule { position: absolute; background: var(--white); }
  .flyer--half .rule { left: 48px; top: 220px; width: 445px; height: 9px; }
  .flyer--small .rule { left: 29px; top: 221px; width: 309px; height: 6px; }

  .intro { position: absolute; color: var(--white); font-weight: 300; white-space: nowrap; }
  .flyer--half .intro { left: 48px; top: 245px; font-size: 15.5px; line-height: 27.5px; }
  .intro .doctor { font-size: 20px; font-weight: 400; }
  .flyer--small .intro { left: 33px; top: 230px; font-size: 15px; line-height: 23px; }

  .swoosh { position: absolute; left: 0; width: 100%; }
  .flyer--half .swoosh { top: 390px; height: 377px; }
  .flyer--small .swoosh { top: 280px; height: 257px; }

  .arrow { position: absolute; }
  .flyer--half .arrow { left: 0; top: 405px; width: 320px; height: 190px; }
  .flyer--small .arrow { left: 0; top: 285px; width: 215px; height: 130px; }

  .arrow-text { position: absolute; color: var(--white); white-space: nowrap; }
  .arrow-text ul { list-style: none; }
  .flyer--half .arrow-text { left: 33px; top: 431px; }
  .flyer--half .arrow-text h3 { font-size: 18px; font-weight: 700; line-height: 24px; margin-bottom: 2px; }
  .flyer--half .arrow-text li { font-size: 14px; line-height: 17px; font-weight: 300; margin-left: 4px; }
  .flyer--small .arrow-text { left: 23px; top: 303px; }
  .flyer--small .arrow-text h3 { font-size: 13px; font-weight: 700; line-height: 18px; margin-bottom: 2px; }
  .flyer--small .arrow-text li { font-size: 10.5px; line-height: 14px; font-weight: 300; }

  .promise-badge {
    position: absolute; left: 224px; top: 292px; width: 127px; height: 127px;
    border-radius: 50%; background: var(--white); border: 7px solid var(--ink);
    display: flex; align-items: center; justify-content: center; text-align: center;
    font-family: "Arimo", Arial, sans-serif; font-size: 15px; line-height: 19px; color: var(--ink);
  }

  .brand-name { position: absolute; color: var(--orange); font-weight: 300; letter-spacing: 0.5px; white-space: nowrap; }
  .flyer--half .brand-name { left: 88px; top: 610px; font-size: 24px; line-height: 30px; }
  .flyer--small .brand-name { left: 61px; top: 428px; font-size: 16px; line-height: 22px; }

  .reviews { position: absolute; font-family: "Arimo", Arial, sans-serif; color: var(--ink); white-space: nowrap; }
  .flyer--half .reviews { left: 89px; top: 665px; font-size: 17px; line-height: 22px; }
  .flyer--small .reviews { left: 62px; top: 465px; font-size: 12px; line-height: 16px; }

  .contact {
    position: absolute; left: 0; width: 100%; text-align: center; white-space: nowrap;
    font-family: "Arimo", Arial, sans-serif; font-weight: 700; color: var(--ink);
  }
  .contact .web { color: var(--orange); }
  .flyer--half .contact { top: 729px; font-size: 15px; line-height: 20px; }
  .flyer--small .contact { top: 510px; font-size: 10px; line-height: 14px; }
</style>
</head>
<body>

<div class="format-label format-label--large">Half a page flyer</div>
<div class="format-label format-label--small">Half a page flyer</div>

<section class="flyer flyer--half">
  <div class="sky"></div>
  <div class="photo" role="img" aria-label="Photo of a man's bare torso and belly in side view"></div>
  <h1 class="headline">Control<br>your weight</h1>
  <div class="rule"></div>
  <p class="intro">by balancing your nervous and digestive system<br>through the Tane Method. The Tane Method, a technique<br>developed by <span class="doctor">Dr. Wenna. Tane,</span> uses physical<br>pressure to manipulate visceral tissue to bring back<br>resiliency and proper functioning of the whole body.</p>

  <svg class="swoosh" viewBox="0 0 513 377" preserveAspectRatio="none" aria-hidden="true">
    <path d="M0,14 C160,70 340,118 513,141 L513,377 L0,377 Z" fill="var(--navy)"/>
    <path d="M0,26 C160,80 340,128 513,150 L513,377 L0,377 Z" fill="var(--white)"/>
    <path d="M0,36 C160,90 340,136 513,156 L513,172 C340,158 160,150 0,150 Z" fill="var(--blue-mid)"/>
    <path d="M0,150 C160,150 340,158 513,172 L513,377 L0,377 Z" fill="var(--white)"/>
  </svg>

  <svg class="arrow" viewBox="0 0 320 190" aria-hidden="true">
    <polygon points="14,32 199,32 199,18 314,104 199,188 199,174 14,174" fill="var(--grey-shadow)"/>
    <polygon points="0,19 185,19 185,4 300,89 185,174 185,160 0,160" fill="var(--orange)" stroke="var(--white)" stroke-width="4"/>
  </svg>
  <div class="arrow-text">
    <h3>Also helps with</h3>
    <ul>
      <li>- Constipation</li>
      <li>- Bloating</li>
      <li>- IBS</li>
      <li>- Psychological eating<br>&nbsp;&nbsp;disorders</li>
    </ul>
  </div>

  <div class="brand-name">Larkfield Tane Therapy</div>
  <p class="reviews">Our practitioner is highly experienced.<br>Please visit our web sites for reviews.</p>
  <p class="contact">Visit our web site <span class="web">LarkfieldTane.com</span> or call 413-908-2617</p>
</section>

<section class="flyer flyer--small">
  <div class="sky"></div>
  <div class="photo" role="img" aria-label="Photo of the therapist working on a client's shoulder"></div>
  <h2 class="headline">Restore your<br>body's natural<br>resiliency and<br>greatly reduce your<br>physical pain through</h2>
  <div class="rule"></div>
  <p class="intro">The Dr. Wenna Tane Method of<br>Structural Integration.</p>

  <svg class="swoosh" viewBox="0 0 358 257" preserveAspectRatio="none" aria-hidden="true">
    <path d="M0,4 C110,45 240,85 358,100 L358,257 L0,257 Z" fill="var(--navy)"/>
    <path d="M0,13 C110,54 240,93 358,107 L358,257 L0,257 Z" fill="var(--white)"/>
    <path d="M0,20 C110,60 240,99 358,111 L358,121 C240,114 110,110 0,110 Z" fill="var(--blue-mid)"/>
    <path d="M0,110 C110,110 240,114 358,121 L358,257 L0,257 Z" fill="var(--white)"/>
  </svg>

  <svg class="arrow" viewBox="0 0 215 130" aria-hidden="true">
    <polygon points="10,22 138,22 138,12 212,70 138,126 138,118 10,118" fill="var(--grey-shadow)"/>
    <polygon points="0,14 130,14 130,3 204,60 130,117 130,108 0,108" fill="var(--orange)" stroke="var(--white)" stroke-width="3"/>
  </svg>
  <div class="arrow-text">
    <h3>Benefits:</h3>
    <ul>
      <li>reduce aches and pain</li>
      <li>reduce joint pain</li>
      <li>reduce chronic</li>
      <li>muscular tension"</li>
    </ul>
  </div>

  <div class="promise-badge">Feel better<br>after the first<br>session!</div>

  <div class="brand-name">Larkfield Tane Therapy</div>
  <p class="reviews">Our practitioner is highly experienced.<br>Please visit our web sites for reviews.</p>
  <p class="contact">Visit our web site <span class="web">LarkfieldTane.com</span> or call 413-908-2617</p>
</section>

</body>
</html>
```